Brixo Tidy Yard Website

We need a website design for this new company. I've attached the Halden Co. This company is in the construction industry that provides general labor, maintenance and cleaning for construction sites. We want a clean and simple website that can be easy to navigate.

Target Market(s)

Construction industry

Industry/Entity Type

Construction

Number of Pages Required

2 page

Font styles to use
Sans Serif

```html
<!DOCTYPE html>
<html lang="en">
<head>
<meta charset="utf-8">
<title>Brixo Tidy Yard</title>
<link rel="stylesheet" href="https://fonts.googleapis.com/css2?family=Archivo:wght@700;800;900&family=Montserrat:wght@400;500;600;700&display=swap">
<style>
:root{
  --navy:#0c0f6b;
  --orange:#f26a10;
  --ink:#222;
  --muted:#555;
  --soft:#f5f6f8;
  --line:#dcdde2;
  --violet:#4b4a9e;
  --white:#fff;
}
*{margin:0;padding:0;box-sizing:border-box}
html,body{width:1200px;height:2368px;overflow:hidden}
body{position:relative;background:var(--white);font-family:"Montserrat",Arial,sans-serif;color:var(--ink)}
.abs{position:absolute}

/* header */
.site-header{left:0;top:0;width:1200px;height:90px;background:var(--white)}
.brand{left:120px;top:26px;display:flex;align-items:center;gap:10px}
.brand-mark{width:22px;height:22px;background:var(--orange)}
.brand-name{font-family:"Archivo",Arial,sans-serif;font-weight:900;font-size:24px;color:var(--navy);letter-spacing:.2px}
.main-nav{left:525px;top:37px;display:flex;gap:36px;font-size:13.5px;font-weight:500;letter-spacing:.4px}
.main-nav a{color:var(--ink);text-decoration:none}
.main-nav a.active{color:var(--orange)}
.phone{left:931px;top:30px;display:flex;align-items:center;gap:10px;font-weight:700;font-size:17px;color:var(--ink)}

/* hero */
.hero{left:0;top:90px;width:1200px;height:510px;overflow:hidden}
.hero-photo{width:100%;height:100%;background:linear-gradient(180deg,#cfcdc6 0%,#d8d4cb 40%,#9d958a 75%,#5a5650 100%)}
.hero-shade{left:0;top:0;width:118px;height:100%;background:rgba(30,30,30,.45)}
.hero-arrow{top:238px;width:34px;height:34px;border:1px solid rgba(255,255,255,.8);display:flex;align-items:center;justify-content:center}
.hero-title{left:0;top:382px;width:1200px;text-align:center;font-family:"Archivo",Arial,sans-serif;font-weight:800;font-size:39px;color:var(--white);text-shadow:0 2px 6px rgba(0,0,0,.45);letter-spacing:-.3px}
.hero-wedge{left:0;top:540px;width:1200px;height:62px}

/* about */
.about-brand{left:120px;top:676px}
.about-brand .name{font-family:"Archivo",Arial,sans-serif;font-weight:900;font-size:68px;line-height:1;color:var(--navy);width:270px}
.about-rule{left:450px;top:676px;width:2px;height:84px;background:var(--navy)}
.about-copy{left:520px;top:672px;width:560px}
.about-copy h2{font-size:17px;font-weight:700;line-height:27px;color:var(--navy)}
.about-copy p{margin-top:12px;font-size:13px;line-height:26.5px;color:var(--ink)}
.read-more{display:inline-block;margin-top:8px;font-size:13px;font-weight:700;color:var(--orange);text-decoration:underline;letter-spacing:.5px}

/* services */
.services{left:0;top:973px;width:1200px;height:630px;background:var(--soft)}
.section-title{width:1200px;left:0;text-align:center;font-family:"Archivo",Arial,sans-serif;font-weight:900;font-size:35px;color:var(--navy);letter-spacing:1px}
.service-card{top:1123px;width:301px;height:390px;background:var(--white);box-shadow:0 2px 6px rgba(0,0,0,.14);text-align:center}
.service-photo{position:absolute;left:0;top:0;width:301px;height:190px}
.service-icon{position:absolute;left:120px;top:153px;width:62px;height:62px;border-radius:50%;background:var(--navy);border:3px solid var(--white);display:flex;align-items:center;justify-content:center}
.service-card h3{position:absolute;top:240px;width:100%;font-family:"Archivo",Arial,sans-serif;font-weight:800;font-size:19px;color:var(--orange);letter-spacing:1px}
.service-card p{position:absolute;top:274px;left:26px;width:249px;font-size:13.5px;line-height:24px;color:var(--ink)}
.service-go{position:absolute;left:135px;top:373px;width:32px;height:32px;border-radius:50%;background:var(--navy);display:flex;align-items:center;justify-content:center}

/* banner */
.banner{left:0;top:1603px;width:1200px;height:345px;background:linear-gradient(180deg,#5553a6 0%,#4b4a9e 55%,#6a66b0 100%)}
.banner-inner{left:0;top:1672px;width:1200px;text-align:center;color:var(--white)}
.banner-inner h2{font-family:"Archivo",Arial,sans-serif;font-weight:800;font-size:29px}
.banner-inner p{margin-top:12px;font-size:22px;line-height:36px}
.btn{display:inline-block;margin-top:20px;padding:12px 18px;background:var(--orange);color:var(--white);font-weight:700;font-size:15px;letter-spacing:.6px}

/* clients */
.client{top:2095px;width:181px;height:93px;border:1px solid var(--line);display:flex;align-items:center;justify-content:center;gap:8px;font-family:"Montserrat",Arial,sans-serif;font-weight:700;font-size:19px;color:#333}
.client i{display:block;width:14px;height:14px;background:#333}

/* footer */
.footer-wedge{left:0;top:2250px;width:1200px;height:52px}
.site-footer{left:0;top:2300px;width:1200px;height:68px;background:var(--navy);color:var(--white)}
.copyright{left:120px;top:2328px;font-size:13px;color:var(--white)}
.footer-brand{left:530px;top:2322px;width:140px;text-align:center;font-family:"Archivo",Arial,sans-serif;font-weight:900;font-size:18px;color:var(--white)}
.social{top:2319px;width:31px;height:31px;border:1.5px solid var(--white);border-radius:50%}
</style>
</head>
<body>

<header class="abs site-header">
  <div class="abs brand"><span class="brand-mark"></span><span class="brand-name">Brixo Tidy Yard</span></div>
  <nav class="abs main-nav">
    <a class="active" href="#">HOME</a><a href="#">ABOUT US</a><a href="#">SERVICES</a><a href="#">CONTACT US</a>
  </nav>
  <div class="abs phone">
    <svg width="22" height="22" viewBox="0 0 22 22"><circle cx="11" cy="11" r="9.5" fill="none" stroke="#f26a10" stroke-width="2"/><path d="M7.5 6.5l2 0 1 2.5-1.3 1a6 6 0 0 0 2.8 2.8l1-1.3 2.5 1v2a1 1 0 0 1-1 1A8 8 0 0 1 6.5 7.5a1 1 0 0 1 1-1z" fill="#f26a10"/></svg>
    555-010-4477
  </div>
</header>

<section class="abs hero">
  <div class="hero-photo" role="img" aria-label="Empty building interior under construction with debris bags and ladders"></div>
  <div class="abs hero-shade"></div>
  <div class="abs hero-arrow" style="left:48px"><svg width="12" height="16"><path d="M9 2L3 8l6 6" fill="none" stroke="#fff" stroke-width="1.5"/></svg></div>
  <div class="abs hero-arrow" style="left:1117px"><svg width="12" height="16"><path d="M3 2l6 6-6 6" fill="none" stroke="#fff" stroke-width="1.5"/></svg></div>
  <h1 class="abs hero-title" style="top:382px">DON’T STRESS WE’LL HANDLE THE MESS</h1>
</section>
<svg class="abs hero-wedge" viewBox="0 0 1200 62" preserveAspectRatio="none"><path d="M0 60 L1200 10 L1200 62 L0 62Z" fill="#f26a10"/></svg>

<section>
  <div class="abs about-brand"><div class="name">Brixo Tidy Yard</div></div>
  <div class="abs about-rule"></div>
  <div class="abs about-copy">
    <h2>About praesent sit amet diam tincidunt, convallis turpis eu, cursus diam mauris porta, neque et viverra aliquet est libero.</h2>
    <p>Lorem ipsum dolor sit amet, consectetur adipiscing elit, sed do eiusmod tempor incididunt ut labore et dolore magna aliqua. Ut enim ad minim veniam, quis nostrud exercitation ullamco laboris nisi ut aliquip ex ea commodo consequat. Duis aute irure dolor in reprehenderit in voluptate velit esse cillum dolore eu fugiat nulla pariatur.</p>
    <a class="read-more" href="#">READ MORE</a>
  </div>
</section>

<section class="abs services"></section>
<h2 class="abs section-title" style="top:1040px">OUR SERVICES</h2>

<article class="abs service-card" style="left:120px">
  <div class="service-photo" role="img" aria-label="Crew in safety vests pouring concrete" style="background:linear-gradient(180deg,#8d8478,#6d665d)"></div>
  <svg class="abs" style="left:0;top:150px" width="301" height="41" viewBox="0 0 301 41"><path d="M0 20 Q150 -20 301 20 L301 41 L0 41Z" fill="#fff"/></svg>
  <div class="service-icon"><svg width="28" height="28" viewBox="0 0 28 28"><circle cx="14" cy="10" r="5" fill="#fff"/><path d="M5 25a9 9 0 0 1 18 0z" fill="#fff"/></svg></div>
  <h3>GENERAL LABOR</h3>
  <p>Donec bibendum orci id molestie blandit. Vestibulum augue nisl, vehicula a fringilla et, tempor nisi.</p>
  <div class="service-go"><svg width="10" height="12"><path d="M3 2l4 4-4 4" fill="none" stroke="#fff" stroke-width="2"/></svg></div>
</article>

<article class="abs service-card" style="left:450px">
  <div class="service-photo" role="img" aria-label="Road maintenance workers at a street site" style="background:linear-gradient(180deg,#9a9487,#6f685e)"></div>
  <svg class="abs" style="left:0;top:150px" width="301" height="41" viewBox="0 0 301 41"><path d="M0 20 Q150 -20 301 20 L301 41 L0 41Z" fill="#fff"/></svg>
  <div class="service-icon"><svg width="28" height="28" viewBox="0 0 28 28"><circle cx="14" cy="14" r="8" fill="none" stroke="#fff" stroke-width="3"/><circle cx="14" cy="14" r="3" fill="#fff"/></svg></div>
  <h3>MAINTENANCE</h3>
  <p>Donec bibendum orci id molestie blandit. Vestibulum augue nisl, vehicula a fringilla et, tempor nisi.</p>
  <div class="service-go"><svg width="10" height="12"><path d="M3 2l4 4-4 4" fill="none" stroke="#fff" stroke-width="2"/></svg></div>
</article>

<article class="abs service-card" style="left:778px">
  <div class="service-photo" role="img" aria-label="Worker pressure washing a concrete floor" style="background:linear-gradient(180deg,#a8a49d,#7a8089)"></div>
  <svg class="abs" style="left:0;top:150px" width="301" height="41" viewBox="0 0 301 41"><path d="M0 20 Q150 -20 301 20 L301 41 L0 41Z" fill="#fff"/></svg>
  <div class="service-icon"><svg width="28" height="28" viewBox="0 0 28 28"><path d="M9 4v14" stroke="#fff" stroke-width="2.5"/><path d="M4 18h10l1 6H3z" fill="#fff"/><circle cx="20" cy="8" r="3" fill="#fff"/><path d="M17 13h6v11h-6z" fill="#fff"/></svg></div>
  <h3>CLEANING</h3>
  <p>Donec bibendum orci id molestie blandit. Vestibulum augue nisl, vehicula a fringilla et, tempor nisi.</p>
  <div class="service-go"><svg width="10" height="12"><path d="M3 2l4 4-4 4" fill="none" stroke="#fff" stroke-width="2"/></svg></div>
</article>

<section class="abs banner" role="img" aria-label="Worker sweeping construction dust, tinted violet"></section>
<div class="abs banner-inner">
  <h2>Brixo Tidy Yard Provides Construction Cleanup Services</h2>
  <p>for clients in various industries, from large jobs to small. We know our clients<br>businesses are growing and changing.</p>
  <a class="btn">CONTACT US TODAY</a>
</div>

<h2 class="abs section-title" style="top:2017px">OUR CLIENTS</h2>
<div class="abs client" style="left:120px"><i style="border-radius:50%"></i>Norvale</div>
<div class="abs client" style="left:315px">Lintwork</div>
<div class="abs client" style="left:509px">Halden Co</div>
<div class="abs client" style="left:704px">Greyfen</div>
<div class="abs client" style="left:898px"><i></i>Quarrow</div>

<svg class="abs footer-wedge" viewBox="0 0 1200 52" preserveAspectRatio="none"><path d="M0 2 L1200 42 L1200 52 L0 52Z" fill="#f26a10"/></svg>
<footer class="abs site-footer"></footer>
<div class="abs copyright">Copyright © 2019 Brixo Tidy Yard. All Rights Reserved.</div>
<div class="abs footer-brand">Brixo Tidy Yard</div>
<a class="abs social" style="left:930px" aria-label="Social profile"></a>
<a class="abs social" style="left:968px" aria-label="Social profile"></a>
<a class="abs social" style="left:1006px" aria-label="Social profile"></a>
<a class="abs social" style="left:1044px" aria-label="Social profile"></a>

</body>
</html>
```